Staffing and Consulting Service Company needs Business Cards

We need to have business cards for our business. You can check our website www.talvrenix.com to see the branding we are using. The logo is in the website.
We use a tag line Staffing & Consulting Solutions Made Easy.
We use different blues in the logo and we use the red for the Company name.
As you can see in the website there is a gradient in the bottom part of each page that includes some of the dots we use for the logo.
We will need the following fields on the design:
Company Name
Employee Name
Title
Address
Tel
Email
Website
Can be Single or Double Sided
There is no preference for single or double sided.
Target Market(s)
Companies in need of IT staffing and IT consulting services
Industry/Entity Type
Business
Look and feel

```html
<!DOCTYPE html>
<html lang="en">
<head>
<meta charset="utf-8">
<title>Talvrenix Business Cards</title>
<link rel="stylesheet" href="https://fonts.googleapis.com/css2?family=EB+Garamond:wght@400;500&family=Arimo:wght@400&display=swap">
<style>
  :root {
    --stage: #7a7a7a;
    --stage-light: #8a8a8a;
    --paper: #ffffff;
    --navy: #243d72;
    --navy-dot: #2f4a82;
    --brand-red: #8a3a44;
    --title-blue: #2b4a8c;
    --ink-light: #ffffff;
    --mark: #c9d2e3;
  }
  * { margin: 0; padding: 0; box-sizing: border-box; }
  html, body { width: 1200px; height: 1000px; overflow: hidden; }
  body {
    background: radial-gradient(ellipse at center, var(--stage-light), var(--stage));
    position: relative;
    font-family: "Arimo", Arial, sans-serif;
  }
  .card {
    position: absolute;
    top: 350px;
    width: 513px;
    height: 300px;
    background: var(--paper);
    box-shadow: 0 3px 8px rgba(0,0,0,0.35);
    overflow: hidden;
  }
  .card--person { left: 55px; }
  .card--brand { left: 632px; }
  .band {
    position: absolute;
    left: 0; right: 0; bottom: 0;
    background: var(--navy);
  }
  .card--person .band { height: 180px; }
  .card--brand .band { height: 125px; }
  .band-texture {
    position: absolute;
    left: 14px; right: 14px; bottom: 12px;
    height: 76px;
    background: linear-gradient(to bottom, rgba(60,88,145,0.15), rgba(60,88,145,0.55));
    border-radius: 4px;
  }
  .person-name {
    position: absolute;
    left: 278px; top: 24px;
    font-family: "EB Garamond", Georgia, serif;
    font-size: 25px;
    color: var(--brand-red);
    letter-spacing: 0.5px;
  }
  .person-title {
    position: absolute;
    left: 278px; top: 54px;
    font-size: 14px;
    color: var(--title-blue);
  }
  .contact {
    position: absolute;
    left: 34px; top: 26px;
    list-style: none;
    color: var(--ink-light);
    font-size: 14px;
    line-height: 20px;
  }
  .contact li { display: flex; align-items: center; gap: 6px; }
  .contact .indent { padding-left: 0; line-height: 17px; }
  .contact svg { width: 10px; height: 10px; fill: var(--ink-light); }
  .brand-lockup {
    position: absolute;
    left: 50px; top: 73px;
    display: flex; align-items: center; gap: 18px;
  }
  .brand-square {
    width: 28px; height: 28px;
    background: var(--navy);
    border-radius: 4px;
  }
  .brand-name {
    font-family: "EB Garamond", Georgia, serif;
    font-size: 60px;
    font-weight: 400;
    color: var(--brand-red);
    letter-spacing: 1px;
    line-height: 1;
  }
  .website {
    position: absolute;
    left: 182px; top: 139px;
    display: flex; align-items: center; gap: 5px;
    font-size: 14px;
    color: var(--title-blue);
  }
  .website svg { width: 10px; height: 10px; }
  .tagline {
    position: absolute;
    left: 0; right: 0; top: 12px;
    text-align: center;
    font-family: "EB Garamond", Georgia, serif;
    font-size: 21px;
    color: var(--ink-light);
  }
</style>
</head>
<body>
  <section class="card card--person">
    <p class="person-name">MARTIN OAKES</p>
    <p class="person-title">Managing Director</p>
    <div class="band">
      <ul class="contact">
        <li><svg viewBox="0 0 10 10"><path d="M2 0.5 L3.6 2.6 L2.8 3.6 Q4 6 6.4 7.2 L7.4 6.4 L9.5 8 L8.4 9.5 Q3 9 0.5 1.6 Z"/></svg>+00 512 480 317</li>
        <li><svg viewBox="0 0 10 10"><rect x="0.5" y="2" width="9" height="6.5" rx="0.8"/><path d="M0.8 2.4 L5 6 L9.2 2.4" stroke="#243d72" stroke-width="0.9" fill="none"/></svg>m.oakes@talvrenix.com</li>
        <li class="indent">7/208 Ferrow road</li>
        <li class="indent">Brandell, Norvania 41</li>
      </ul>
      <div class="band-texture" role="img" aria-label="Faint dot pattern fading across the blue band"></div>
    </div>
  </section>

  <section class="card card--brand">
    <div class="brand-lockup">
      <span class="brand-square"></span>
      <span class="brand-name">TALVRENIX</span>
    </div>
    <p class="website">
      <svg viewBox="0 0 10 10"><circle cx="5" cy="5" r="4.5" fill="#2b4a8c"/><path d="M0.5 5 H9.5 M5 0.5 V9.5 M1.5 2.8 H8.5 M1.5 7.2 H8.5" stroke="#fff" stroke-width="0.6" fill="none"/><ellipse cx="5" cy="5" rx="2" ry="4.5" stroke="#fff" stroke-width="0.6" fill="none"/></svg>
      www.talvrenix.com
    </p>
    <div class="band">
      <p class="tagline">Staffing &amp; Consulting Solutions Made Easy</p>
      <div class="band-texture" role="img" aria-label="Faint dot pattern fading across the blue band"></div>
    </div>
  </section>
</body>
</html>
```